Chilled (açaí bowls)

I’m starting a Portable açaí bowl business for TV and movie sets, I have a little ice cream cart with an umbrella, and I’m a petite Brown haired young woman. I’d like to either put a silhouette of myself into the card or just the ice cream cart or something more creative, I have no idea what it should look like yet

Target Market(s)

Entertainment industry craft service officials

Contact Information for Business Card

Would love it to be somewhat colorful

Colors

Designer to choose colors to be used in the design.

Requirements
Must have
• Nora Patchett
• Norabyday@fernmail.example
• 310-428-9073
• Chilled (Business name)
Nice to have
• Ice cream cart w/ umbrella

```html
<!DOCTYPE html>
<html lang="en">
<head>
<meta charset="utf-8">
<title>Chilled – Business Card</title>
<link href="https://fonts.googleapis.com/css2?family=Open+Sans:wght@600;700&family=Lato:wght@400;700&display=swap" rel="stylesheet">
<style>
  :root {
    --page-bg: #e6e8eb;
    --card-bg: #ffffff;
    --brand-blue: #1f74c0;
    --ink: #222326;
    --tagline: #3a3b3e;
    --cart-light: #f3f6f9;
    --cart-blue: #5aa8e6;
    --card-shadow: rgba(0,0,0,0.18);
  }
  * { margin: 0; padding: 0; box-sizing: border-box; }
  html, body { width: 1200px; height: 1200px; overflow: hidden; }
  body {
    background: var(--page-bg);
    font-family: "Open Sans", sans-serif;
    position: relative;
  }
  .card {
    position: absolute;
    left: 150px;
    width: 900px;
    height: 514px;
    background: var(--card-bg);
    box-shadow: 0 10px 30px var(--card-shadow);
  }
  .card--front { top: 60px; }
  .card--back { top: 626px; }

  .cart-art {
    position: absolute;
    left: 60px;
    top: 80px;
    width: 330px;
    height: 370px;
    border-radius: 18px;
    background: linear-gradient(160deg, var(--cart-light) 0%, #cfe3f5 45%, var(--cart-blue) 100%);
  }

  .brand-name {
    position: absolute;
    font-family: "Open Sans", sans-serif;
    font-weight: 700;
    color: var(--brand-blue);
    line-height: 1;
    letter-spacing: -1px;
  }
  .card--front .brand-name { left: 420px; top: 160px; font-size: 132px; }
  .tagline {
    position: absolute;
    left: 432px;
    top: 310px;
    font-family: "Open Sans", sans-serif;
    font-weight: 600;
    font-size: 34px;
    letter-spacing: 3px;
    color: var(--tagline);
  }

  .card--back .brand-name { left: 420px; top: 70px; font-size: 120px; }
  .contact {
    position: absolute;
    right: 60px;
    top: 250px;
    text-align: right;
    font-family: "Lato", sans-serif;
    color: var(--ink);
  }
  .contact__name {
    font-family: "Open Sans", sans-serif;
    font-weight: 600;
    font-size: 34px;
    color: var(--brand-blue);
    line-height: 1.1;
  }
  .contact__role { font-size: 22px; margin-bottom: 14px; }
  .contact__line {
    display: flex;
    justify-content: flex-end;
    align-items: center;
    gap: 8px;
    font-size: 24px;
    line-height: 1.5;
  }
  .contact__icon { width: 20px; height: 20px; flex: none; }
  .contact__icon-spacer { width: 20px; flex: none; }
</style>
</head>
<body>

  <section class="card card--front">
    <div class="cart-art" role="img" aria-label="Ice cream cart with a blue and white umbrella"></div>
    <div class="brand-name">Chilled</div>
    <div class="tagline">Ice Cream Cart</div>
  </section>

  <section class="card card--back">
    <div class="cart-art" role="img" aria-label="Ice cream cart with a blue and white umbrella"></div>
    <div class="brand-name">Chilled</div>
    <div class="contact">
      <div class="contact__name">Nora Patchett</div>
      <div class="contact__role">owner</div>
      <div class="contact__line">
        <span>310-428-9073</span>
        <svg class="contact__icon" viewBox="0 0 24 24" aria-hidden="true">
          <path d="M6.6 10.8a15 15 0 0 0 6.6 6.6l2.2-2.2a1 1 0 0 1 1-.25 11.4 11.4 0 0 0 3.6.57 1 1 0 0 1 1 1V20a1 1 0 0 1-1 1A17 17 0 0 1 3 4a1 1 0 0 1 1-1h3.5a1 1 0 0 1 1 1c0 1.25.2 2.45.57 3.6a1 1 0 0 1-.25 1z" fill="var(--brand-blue)"/>
        </svg>
      </div>
      <div class="contact__line">
        <span>Norabyday@fernmail.example</span>
        <svg class="contact__icon" viewBox="0 0 24 24" aria-hidden="true">
          <rect x="3" y="6" width="18" height="13" rx="2" fill="none" stroke="var(--brand-blue)" stroke-width="2"/>
          <path d="M3 7l9 6 9-6" fill="none" stroke="var(--brand-blue)" stroke-width="2"/>
        </svg>
      </div>
    </div>
  </section>

</body>
</html>
```